Velqor5 Business Card - Health

Velqor5 maximizes value from the health data of its clients, including doctors, HMOs, and patients. I have attached the Velqor5 logo as an ai and eps file.
Target Market(s)
Health, HMO, Healthcare, Data, Big Data, Data Analytics
Industry/Entity Type
Business
Requirements
Must have
- At least one side should have some white on it so that we can write on it.

```html
<!DOCTYPE html>
<html lang="en">
<head>
<meta charset="utf-8">
<title>Velqor5 Business Card</title>
<link rel="stylesheet" href="https://fonts.googleapis.com/css2?family=Questrial&family=Jost:wght@400&display=swap">
<style>
  :root {
    --backdrop: #8a8b8b;
    --card-dark: #2b2b2b;
    --card-white: #ffffff;
    --blue-light: #0aa0ea;
    --blue-mid: #0a8fe0;
    --blue-deep: #0a66c8;
    --ink: #2a2a2a;
    --ink-soft: #4a4a4a;
    --rule: #c9c9c9;
  }
  * { margin: 0; padding: 0; box-sizing: border-box; }
  html, body { width: 1200px; height: 900px; overflow: hidden; }
  body { background: var(--backdrop); position: relative; font-family: "Jost", sans-serif; }

  .card {
    position: absolute;
    left: 321px;
    width: 507px;
    height: 290px;
    overflow: hidden;
  }
  .card--front { top: 119px; background: var(--card-dark); }
  .card--back { top: 471px; background: var(--card-white); }

  /* Front */
  .front-art { position: absolute; left: 0; top: 0; width: 507px; height: 290px; }
  .front-brand {
    position: absolute;
    right: 36px;
    top: 200px;
    text-align: right;
    color: #fff;
  }
  .front-brand__name {
    font-family: "Questrial", sans-serif;
    font-size: 50px;
    line-height: 1;
    letter-spacing: -0.5px;
  }
  .front-brand__web {
    font-family: "Questrial", sans-serif;
    font-size: 12px;
    letter-spacing: 3.6px;
    margin-top: 6px;
  }

  /* Back */
  .back-brand {
    position: absolute;
    left: 57px;
    top: 122px;
    display: flex;
    align-items: center;
    gap: 14px;
  }
  .back-brand__dot {
    width: 48px; height: 48px;
    border-radius: 50%;
    background: var(--blue-mid);
  }
  .back-brand__name {
    font-family: "Questrial", sans-serif;
    font-size: 44px;
    line-height: 1;
    color: var(--ink);
  }
  .divider {
    position: absolute;
    left: 272px;
    top: 66px;
    width: 1px;
    height: 180px;
    background: var(--rule);
  }
  .contact {
    position: absolute;
    left: 294px;
    top: 62px;
    color: var(--ink-soft);
  }
  .contact__name { font-size: 22px; line-height: 1.1; color: var(--blue-deep); }
  .contact__role { font-size: 16px; line-height: 1.2; color: var(--blue-light); }
  .contact__address { font-size: 13px; line-height: 16px; margin-top: 9px; }
  .contact__list { list-style: none; margin-top: 6px; }
  .contact__list li {
    display: flex;
    align-items: center;
    gap: 6px;
    font-size: 13px;
    line-height: 19.5px;
  }
  .contact__list svg { width: 14px; height: 14px; fill: var(--blue-deep); flex: none; }

  .web-band {
    position: absolute;
    left: 0; top: 253px;
    width: 507px; height: 23px;
    background: var(--blue-light);
  }
  .web-band__accent {
    position: absolute;
    left: 0; top: 0;
    width: 166px; height: 23px;
    background: var(--blue-deep);
  }
  .web-band__text {
    position: absolute;
    left: 178px; top: 3px;
    color: #fff;
    font-size: 12px;
    font-style: italic;
    letter-spacing: 3.6px;
  }
</style>
</head>
<body>

<section class="card card--front">
  <svg class="front-art" viewBox="0 0 507 290" role="img" aria-label="Geometric blue brand artwork area">
    <defs>
      <linearGradient id="artGradient" x1="0" y1="0" x2="1" y2="1">
        <stop offset="0" stop-color="#0aa0ea"/>
        <stop offset="1" stop-color="#0a6fd0"/>
      </linearGradient>
    </defs>
    <polygon points="0,0 238,0 275,166 180,290 0,290" fill="url(#artGradient)"/>
  </svg>
  <div class="front-brand">
    <div class="front-brand__name">Velqor5</div>
    <div class="front-brand__web">www.velqor5.com</div>
  </div>
</section>

<section class="card card--back">
  <div class="back-brand">
    <span class="back-brand__dot"></span>
    <span class="back-brand__name">Velqor5</span>
  </div>

  <div class="divider"></div>

  <div class="contact">
    <div class="contact__name">Marta Lindqvist</div>
    <div class="contact__role">CEO/Founder</div>
    <div class="contact__address">4120 Harbor Ridge Way<br>Juneau, Alaska 99801</div>
    <ul class="contact__list">
      <li>
        <svg viewBox="0 0 24 24"><path d="M6.6 10.8a15 15 0 0 0 6.6 6.6l2.2-2.2a1 1 0 0 1 1-.25 11.4 11.4 0 0 0 3.6.57 1 1 0 0 1 1 1V20a1 1 0 0 1-1 1A17 17 0 0 1 3 4a1 1 0 0 1 1-1h3.5a1 1 0 0 1 1 1c0 1.25.2 2.45.57 3.6a1 1 0 0 1-.25 1z"/></svg>
        907 512 4418
      </li>
      <li>
        <svg viewBox="0 0 24 24"><path d="M7 1h10a2 2 0 0 1 2 2v18a2 2 0 0 1-2 2H7a2 2 0 0 1-2-2V3a2 2 0 0 1 2-2zm0 3v14h10V4zm5 15.5a1.2 1.2 0 1 0 0 2.4 1.2 1.2 0 0 0 0-2.4z"/></svg>
        907 771 2093
      </li>
      <li>
        <svg viewBox="0 0 24 24"><path d="M6 2h12v6H6zM3 9h18a2 2 0 0 1 2 2v7h-4v4H5v-4H1v-7a2 2 0 0 1 2-2zm4 8v3h10v-3z"/></svg>
        907 364 8825
      </li>
      <li>
        <svg viewBox="0 0 24 24"><path d="M2 5h20v14H2zm2 2v.5l8 5 8-5V7zm0 2.8V17h16V9.8l-8 5z"/></svg>
        hello@velqor5.com
      </li>
    </ul>
  </div>

  <div class="web-band">
    <div class="web-band__accent"></div>
    <div class="web-band__text">www.velqor5.com</div>
  </div>
</section>

</body>
</html>
```